Downtown hair salon need trendy website

I need a website with style. Unique. We need this site to list prices , Hair and nail services, service providers hours. I would also like my logo design on the website. We are located Downtown Riverton Falls. Beautiful city with lots of culture.

Target Market(s)

Men and women

Industry/Entity Type

Hair And Beauty

Coding

Coded - Design and coding required

Number of Pages Required

3 page

Font styles to use
Sans Serif

Colors

Designer to choose colors to be used in the design.

Requirements
Must have
• Logo of business. Hours, services and prices, Page for pictures of each service provider. Nail service and prices. Products that we carry... Area on page for my mission statement.
Nice to have
• Pictures of trendy of the beauty industry. Men and women cuts.. Nails..
Should not have
• booking on line options...

```html
<!DOCTYPE html>
<html lang="en">
<head>
<meta charset="utf-8">
<title>Lumora Downtown — Services</title>
<link rel="stylesheet" href="https://fonts.googleapis.com/css2?family=Poppins:wght@300;400;500&family=Libre+Baskerville:wght@700&display=swap">
<style>
:root{
  --gold:#c9952e;
  --gold-soft:#d2a248;
  --bg:#1f1809;
  --panel:#040302;
  --text:#d9d1c1;
  --muted:#a89d88;
  --line:rgba(201,149,46,.22);
  --white:#ffffff;
}
*{box-sizing:border-box;margin:0;padding:0}
html,body{width:1200px;height:4886px;overflow:hidden}
body{background:var(--bg);color:var(--text);font-family:'Poppins',sans-serif;position:relative}

/* Header / hero */
.hero{position:absolute;left:0;top:0;width:1200px;height:413px;
  background:linear-gradient(180deg,rgba(20,14,8,.55),rgba(20,14,8,.8)),
  linear-gradient(90deg,#5a4a3e 0%,#8a7564 30%,#4b3a2e 55%,#7d6a5b 75%,#3c2f25 100%)}
.brand{position:absolute;left:161px;top:40px;width:118px;text-align:center;color:var(--gold);font-family:'Poppins',sans-serif;font-weight:400}
.brand .name{font-size:24px;letter-spacing:1px;line-height:28px;display:block}
.brand .sub{font-size:9px;letter-spacing:3px;line-height:14px;display:block}
.top-contact{position:absolute;right:160px;top:20px;display:flex;gap:26px;font-size:11.5px;color:var(--white)}
.top-contact span{display:flex;align-items:center;gap:8px}
.main-nav{position:absolute;left:442px;top:78px;display:flex;gap:42px;list-style:none;font-size:12px;color:var(--white);letter-spacing:.3px}
.main-nav li.active{position:relative}
.main-nav li.active::after{content:"";position:absolute;left:0;right:0;bottom:-8px;height:2px;background:var(--gold)}
.title-frame{position:absolute;left:322px;top:195px;width:554px;height:95px;border:1px solid rgba(201,149,46,.7)}
.title-frame::before{content:"";position:absolute;inset:6px -6px;border:1px solid rgba(201,149,46,.45)}
.hero-title{position:absolute;left:322px;top:224px;width:554px;text-align:center;font-family:'Libre Baskerville',serif;font-weight:700;font-size:31px;line-height:38px;color:var(--white);letter-spacing:.5px}
.crumbs{position:absolute;left:161px;top:384px;font-size:11px;color:var(--white);display:flex;gap:18px;align-items:center}
.crumbs .current{color:var(--gold)}

/* Section titles */
.eyebrow{position:absolute;left:0;width:1200px;text-align:center;color:var(--gold);font-size:15px;font-weight:300;letter-spacing:.5px}
.section-title{position:absolute;left:0;width:1200px;text-align:center;color:var(--gold);font-size:28px;font-weight:300;letter-spacing:1px}
.scissors{position:absolute;left:588px}

/* Services overview */
.photo{position:absolute;left:0;width:563px}
.photo .frame{position:absolute;inset:22px 12px 22px 40px;border:1px solid rgba(255,255,255,.85)}
.photo-stylist{top:650px;height:450px;background:linear-gradient(135deg,#c8a88a 0%,#e6d2bd 40%,#9c7f66 70%,#3d3028 100%)}
.photo-man{top:1103px;height:446px;background:linear-gradient(160deg,#4d5964 0%,#7a6a5c 45%,#3f3226 75%,#2a323a 100%)}
.service-panel{position:absolute;left:563px;top:734px;width:637px;height:728px;background:var(--panel);padding:54px 0 0 36px}
.service-item{width:440px;margin-bottom:30px}
.service-item h3{font-weight:300;font-size:21px;line-height:30px;color:var(--gold);margin-bottom:8px}
.service-item p{font-size:11.5px;line-height:20px;color:var(--text)}

/* Price list */
.price-panel{position:absolute;left:161px;top:1608px;width:878px;height:1941px;background:var(--panel)}
.price-group{position:absolute;left:29px;width:820px}
.price-group h2{font-weight:300;font-size:21px;line-height:28px;color:var(--gold);text-align:center;margin-bottom:18px;letter-spacing:.5px}
.price-table{border-collapse:collapse;width:820px;font-size:11.5px}
.price-table td{height:30.5px;border-bottom:1px solid var(--line);border-left:1px solid var(--line);text-align:center;color:var(--gold);width:84px}
.price-table td.item{text-align:left;color:var(--text);width:316px;padding-left:43px;border-left:none}
.price-table tr:first-child td{border-top:1px solid var(--line)}
.price-table td:last-child{border-right:1px solid var(--line)}
.group-cuts{top:44px}
.group-color{top:469px}
.group-perm{top:801px}
.group-wax{top:1013px}
.group-nails{top:1224px}
.group-nails .price-table{width:736px}
.group-nails h2{width:820px}

/* Contact */
.phone-big{position:absolute;left:0;width:1200px;top:3775px;text-align:center;font-size:34px;color:var(--white);font-weight:400;letter-spacing:1px}
.info-row{position:absolute;top:3866px;left:161px;width:878px;height:96px;display:flex}
.info-col{display:flex;gap:14px}
.info-col h4{color:var(--gold);font-size:13px;font-weight:500;margin-bottom:12px}
.info-col p{font-size:11.5px;line-height:21px;color:var(--white)}
.col-address{width:195px;border-right:1px solid rgba(255,255,255,.12)}
.col-phone{width:280px;padding-left:12px;border-right:1px solid rgba(255,255,255,.12)}
.col-hours{padding-left:12px}
.hours{display:grid;grid-template-columns:74px 96px 76px 80px;font-size:11.5px;line-height:21px;color:var(--white)}
.tools-strip{position:absolute;left:0;top:3996px;width:1200px;height:82px;background:linear-gradient(180deg,#1f1809,#111 40%,#2a2620 100%)}
.map{position:absolute;left:0;top:4078px;width:1200px;height:684px;background:linear-gradient(180deg,#4c463d,#3e392f 60%,#35302a)}
.map-marker{position:absolute;left:522px;top:4207px;width:154px;height:86px;background:var(--white);border-radius:6px;text-align:center;color:var(--gold);padding-top:22px}
.map-marker .name{font-size:20px;line-height:24px;display:block;font-weight:400}
.map-marker .sub{font-size:8px;letter-spacing:3px;display:block;font-weight:400}
.map-pin{position:absolute;left:583px;top:4302px}

/* Inquiry */
.inquiry{position:absolute;left:161px;top:4385px;width:878px;height:377px;background:linear-gradient(135deg,#c8942e,#d4a447 50%,#bf8b26)}
.inquiry-title{position:absolute;left:68px;top:118px;color:var(--white);font-size:28px;line-height:38px;font-weight:400;letter-spacing:1px}
.inquiry-icon{position:absolute;left:70px;top:66px}
.field{position:absolute;width:240px;border-bottom:1px solid rgba(255,255,255,.6);font-size:11.5px;color:var(--white);padding-bottom:12px}
.f-first{left:292px;top:60px}.f-last{left:601px;top:60px}
.f-phone{left:292px;top:113px}.f-email{left:601px;top:113px}
.f-msg{left:292px;top:162px;width:549px;height:70px}
.submit{position:absolute;left:292px;top:282px;width:533px;height:30px;background:#0a0805;color:var(--white);font-size:13px;font-weight:500;text-align:center;line-height:30px;letter-spacing:.5px}
.submit svg{position:absolute;right:-8px;top:-6px}

/* Footer */
.copyright{position:absolute;left:161px;top:4812px;font-size:11.5px;color:var(--white)}
.social{position:absolute;left:868px;top:4806px;display:flex;gap:8px}
.social span{width:28px;height:28px;border:1.5px solid var(--gold);border-radius:50%;display:block}
</style>
</head>
<body>

<header class="hero" role="img" aria-label="Women with long wavy hair seen from behind in a salon, darkened"></header>
<div class="brand"><span class="name">LUMORA</span><span class="sub">DOWNTOWN</span></div>
<div class="top-contact">
  <span><svg width="14" height="14" viewBox="0 0 24 24" fill="#c9952e"><path d="M6.6 10.8a15 15 0 006.6 6.6l2.2-2.2c.3-.3.7-.4 1-.2 1.1.4 2.3.6 3.6.6.6 0 1 .4 1 1V20c0 .6-.4 1-1 1A17 17 0 013 4c0-.6.4-1 1-1h3.5c.6 0 1 .4 1 1 0 1.3.2 2.5.6 3.6.1.3 0 .7-.2 1z"/></svg>555.014.2290</span>
  <span><svg width="14" height="14" viewBox="0 0 24 24" fill="#c9952e"><path d="M2 11l20-9-9 20-2-9z"/></svg>hello@lumoradowntown.com</span>
</div>
<ul class="main-nav">
  <li class="active">HOME</li><li>SERVICES</li><li>TEAM</li><li>ABOUT</li><li>OUR WORK</li><li>BLOG</li><li>CONTACT US</li>
</ul>
<div class="title-frame"></div>
<h1 class="hero-title">TAKE CARE OF YOUR HAIR</h1>
<nav class="crumbs"><span>HOME</span><span>›</span><span class="current">SERVICES</span></nav>

<svg class="scissors" style="top:490px" width="24" height="32" viewBox="0 0 24 32" fill="none" stroke="#8c7a5a" stroke-width="1.4"><path d="M6 2l10 20M18 2L8 22"/><circle cx="7" cy="26" r="4"/><circle cx="17" cy="26" r="4"/></svg>
<div class="eyebrow" style="top:544px">WHAT WE OFFER</div>
<div class="section-title" style="top:570px">SERVICES</div>

<div class="photo photo-stylist" role="img" aria-label="Stylist styling a smiling woman's blonde wavy hair"><div class="frame"></div></div>
<div class="photo photo-man" role="img" aria-label="Young man with dark curly hair in a shearling jacket"><div class="frame"></div></div>

<section class="service-panel">
  <div class="service-item"><h3>Cut &amp; Style</h3><p>We Specialize in Women's, Men's haircuts. Price from Women's cut $29 to $ 59. Men's cuts range from $19 to $ 49. Depending on the level of our Stylists you choose.</p></div>
  <div class="service-item"><h3>Highlights:</h3><p>We offer full highlights, which cover entire head, or partial highlight which covers crown of head. Price range from $69 to $119 depending on level of stylist and foil placements.</p></div>
  <div class="service-item"><h3>Hair Extensions:</h3><p>Consultation are required.</p></div>
  <div class="service-item"><h3>Color:</h3><p>All over color Roots to end $49 to $79 this depends on level of stylists.</p></div>
  <div class="service-item"><h3>Balayage:</h3><p>This is free hand painting of color to give a movable free flowing look. We range from $74 to $99 an hour depending the stylist level you choose.</p></div>
  <div class="service-item"><h3>Treatments:</h3><p>This is free hand painting of color to give a movable free flowing look. We range from $74 to $99 an hour depending the stylist level you choose.</p></div>
</section>

<section class="price-panel">
  <div class="price-group group-cuts">
    <h2>HAIRCUTS &amp; STYLES</h2>
    <table class="price-table">
      <tr><td class="item">Cut &amp; Style</td><td>29.00</td><td>35.00</td><td>41.00</td><td>47.00</td><td>53.00</td><td>59.00</td></tr>
      <tr><td class="item">Barber Cut</td><td>19.00</td><td>25.00</td><td>31.00</td><td>37.00</td><td>43.00</td><td>49.00</td></tr>
      <tr><td class="item">Child's Haircut &lt;12</td><td>19.00</td><td>25.00</td><td>31.00</td><td>37.00</td><td>43.00</td><td>49.00</td></tr>
      <tr><td class="item">Beard Trim</td><td>05.00</td><td>05.00</td><td>05.00</td><td>05.00</td><td>05.00</td><td>05.00</td></tr>
      <tr><td class="item">Bang Trim</td><td>12.00</td><td>12.00</td><td>12.00</td><td>12.00</td><td>12.00</td><td>12.00</td></tr>
      <tr><td class="item">Special Occasion</td><td>44.00</td><td>49.00</td><td>54.00</td><td>59.00</td><td>64.00</td><td>69.00</td></tr>
      <tr><td class="item">Extra Time (Flat Iron, etc.)</td><td>10.00</td><td>10.00</td><td>10.00</td><td>10.00</td><td>10.00</td><td>10.00</td></tr>
      <tr><td class="item">Shampoo Blow Dry</td><td>19.00</td><td>25.00</td><td>31.00</td><td>37.00</td><td>43.00</td><td>49.00</td></tr>
      <tr><td class="item">Luxury Blow Out</td><td>36.00</td><td>39.00</td><td>42.00</td><td>45.00</td><td>48.00</td><td>51.00</td></tr>
      <tr><td class="item">Hair Treatment</td><td>15.00</td><td>15.00</td><td>15.00</td><td>15.00</td><td>15.00</td><td>15.00</td></tr>
      <tr><td class="item">Bond Builder - Luxury Treatment</td><td>45.00</td><td>45.00</td><td>45.00</td><td>45.00</td><td>45.00</td><td>45.00</td></tr>
    </table>
  </div>

  <div class="price-group group-color">
    <h2>COLOR</h2>
    <table class="price-table">
      <tr><td class="item">Color; up to 4oz maximum</td><td>49.00</td><td>55.00</td><td>61.00</td><td>67.00</td><td>73.00</td><td>79.00</td></tr>
      <tr><td class="item">Additional Color; 1oz</td><td>10.00</td><td>10.00</td><td>10.00</td><td>10.00</td><td>10.00</td><td>10.00</td></tr>
      <tr><td class="item">Corrective Color; per hour</td><td>60.00</td><td>60.00</td><td>60.00</td><td>60.00</td><td>60.00</td><td>60.00</td></tr>
      <tr><td class="item">Partial Foils; 11 to 30 foils</td><td>69.00</td><td>75.00</td><td>81.00</td><td>87.00</td><td>93.00</td><td>99.00</td></tr>
      <tr><td class="item">Full Foils; 31+ foils</td><td>89.00</td><td>95.00</td><td>101.00</td><td>107.00</td><td>113.00</td><td>119.00</td></tr>
      <tr><td class="item">&lt; 10 Foils; per foil</td><td>06.00</td><td>06.00</td><td>06.00</td><td>06.00</td><td>06.00</td><td>06.00</td></tr>
      <tr><td class="item">Balyage/Ombre'</td><td>74.00</td><td>79.00</td><td>84.00</td><td>89.00</td><td>94.00</td><td>99.00</td></tr>
      <tr><td class="item">Men's Partial Color</td><td>29.00</td><td>34.00</td><td>39.00</td><td>44.00</td><td>49.00</td><td>54.00</td></tr>
    </table>
  </div>

  <div class="price-group group-perm">
    <h2>PERM</h2>
    <table class="price-table">
      <tr><td class="item">Full Perm; 31+ rods</td><td>49.00</td><td>55.00</td><td>61.00</td><td>67.00</td><td>73.00</td><td>79.00</td></tr>
      <tr><td class="item">&lt;10 Rods; per rod</td><td>10.00</td><td>10.00</td><td>10.00</td><td>10.00</td><td>10.00</td><td>10.00</td></tr>
      <tr><td class="item">Keratin Smoothing</td><td>60.00</td><td>60.00</td><td>60.00</td><td>60.00</td><td>60.00</td><td>60.00</td></tr>
      <tr><td class="item">Keratin Smoothing Split End Repair</td><td>69.00</td><td>75.00</td><td>81.00</td><td>87.00</td><td>93.00</td><td>99.00</td></tr>
    </table>
  </div>

  <div class="price-group group-wax">
    <h2>FACIAL WAX</h2>
    <table class="price-table">
      <tr><td class="item">Brow</td><td>15.00</td><td>15.00</td><td>15.00</td><td>15.00</td><td>15.00</td><td>15.00</td></tr>
      <tr><td class="item">Lip</td><td>10.00</td><td>10.00</td><td>10.00</td><td>10.00</td><td>10.00</td><td>10.00</td></tr>
      <tr><td class="item">Chin</td><td>10.00</td><td>10.00</td><td>10.00</td><td>10.00</td><td>10.00</td><td>10.00</td></tr>
      <tr><td class="item">Full Face</td><td>30.00</td><td>30.00</td><td>30.00</td><td>30.00</td><td>30.00</td><td>30.00</td></tr>
    </table>
  </div>

  <div class="price-group group-nails">
    <h2>NAILS</h2>
    <table class="price-table">
      <tr><td class="item">Regular Manicure</td><td>24.00</td><td>29.00</td><td>34.00</td><td>39.00</td><td>44.00</td></tr>
      <tr><td class="item">Spa Manicure</td><td>29.00</td><td>34.00</td><td>39.00</td><td>44.00</td><td>49.00</td></tr>
      <tr><td class="item">Gel Maniure</td><td>34.00</td><td>39.00</td><td>44.00</td><td>49.00</td><td>54.00</td></tr>
      <tr><td class="item">Gel Polish Upgrade</td><td>34.00</td><td>39.00</td><td>44.00</td><td>49.00</td><td>54.00</td></tr>
      <tr><td class="item">Polish Change</td><td>14.00</td><td>14.00</td><td>14.00</td><td>14.00</td><td>14.00</td></tr>
      <tr><td class="item">Regular Pedicure</td><td>37.00</td><td>40.00</td><td>43.00</td><td>47.00</td><td>51.00</td></tr>
      <tr><td class="item">Spa Pedicure</td><td>42.00</td><td>45.00</td><td>48.00</td><td>51.00</td><td>55.00</td></tr>
      <tr><td class="item">Gel Polish Upgrade</td><td>10.00</td><td>10.00</td><td>10.00</td><td>10.00</td><td>10.00</td></tr>
      <tr><td class="item">Paraffin Treatment</td><td>15.00</td><td>15.00</td><td>15.00</td><td>15.00</td><td>15.00</td></tr>
      <tr><td class="item">Polish Change</td><td>14.00</td><td>14.00</td><td>14.00</td><td>14.00</td><td>14.00</td></tr>
      <tr><td class="item">Acrylic Full Set</td><td>37.00</td><td>40.00</td><td>43.00</td><td>47.00</td><td>51.00</td></tr>
      <tr><td class="item">Acrylic Fill In</td><td>28.00</td><td>31.00</td><td>34.00</td><td>35.00</td><td>39.00</td></tr>
      <tr><td class="item">Gel Full Set</td><td>37.00</td><td>40.00</td><td>43.00</td><td>47.00</td><td>51.00</td></tr>
      <tr><td class="item">Gel Fill In</td><td>28.00</td><td>31.00</td><td>34.00</td><td>35.00</td><td>39.00</td></tr>
      <tr><td class="item">Dipping Powder Full Set</td><td>37.00</td><td>40.00</td><td>43.00</td><td>47.00</td><td>51.00</td></tr>
      <tr><td class="item">Dipping Powder Fill In</td><td>28.00</td><td>31.00</td><td>34.00</td><td>35.00</td><td>39.00</td></tr>
      <tr><td class="item">Repair; each</td><td>09.00</td><td>09.00</td><td>09.00</td><td>09.00</td><td>09.00</td></tr>
      <tr><td class="item">Nail Art; each</td><td>09.00</td><td>09.00</td><td>09.00</td><td>09.00</td><td>09.00</td></tr>
      <tr><td class="item">Application; 1/2 Hour</td><td>29.00</td><td>31.00</td><td>33.00</td><td>35.00</td><td>37.00</td></tr>
      <tr><td class="item">Application; 1 Hour</td><td>49.00</td><td>51.00</td><td>53.00</td><td>55.00</td><td>57.00</td></tr>
      <tr><td class="item">Lesson</td><td>59.00</td><td>61.00</td><td>63.00</td><td>65.00</td><td>67.00</td></tr>
    </table>
  </div>
</section>

<svg class="scissors" style="top:3618px" width="24" height="32" viewBox="0 0 24 32" fill="none" stroke="#8c7a5a" stroke-width="1.4"><path d="M6 2l10 20M18 2L8 22"/><circle cx="7" cy="26" r="4"/><circle cx="17" cy="26" r="4"/></svg>
<div class="eyebrow" style="top:3681px">LUMORA DOWNTOWN</div>
<div class="section-title" style="top:3709px">WE INVITE YOU TO CONTACT US</div>
<div class="phone-big">555.014.2290</div>

<section class="info-row">
  <div class="info-col col-address">
    <svg width="18" height="24" viewBox="0 0 18 24"><path d="M9 1a8 8 0 00-8 8c0 6 8 14 8 14s8-8 8-14a8 8 0 00-8-8z" fill="#c9952e"/><circle cx="9" cy="9" r="3" fill="#1f1809"/></svg>
    <div><h4>Address</h4><p>14 Larch Avenue, Unit 2,<br>Riverton Falls, 10458</p></div>
  </div>
  <div class="info-col col-phone">
    <svg width="24" height="24" viewBox="0 0 24 24" fill="#c9952e"><path d="M6.6 10.8a15 15 0 006.6 6.6l2.2-2.2c.3-.3.7-.4 1-.2 1.1.4 2.3.6 3.6.6.6 0 1 .4 1 1V20c0 .6-.4 1-1 1A17 17 0 013 4c0-.6.4-1 1-1h3.5c.6 0 1 .4 1 1 0 1.3.2 2.5.6 3.6.1.3 0 .7-.2 1z"/></svg>
    <div><h4>Phone / E-mail:</h4><p>555-014-2290<br>hello@lumoradowntown.com</p></div>
  </div>
  <div class="info-col col-hours">
    <svg width="28" height="28" viewBox="0 0 28 28" fill="none" stroke="#c9952e" stroke-width="2"><circle cx="14" cy="14" r="12"/><path d="M14 7v7h6"/></svg>
    <div><h4>Hours of Operation</h4>
      <div class="hours">
        <span>Monday</span><span>Closed</span><span>Thursday</span><span>10 am–7 pm</span>
        <span>Tuesday</span><span>10 am–7 pm</span><span>Friday</span><span>10 am–6 pm</span>
        <span>Wednesday</span><span>10 am–7 pm</span><span>Saturday</span><span>10 am–3 pm</span>
      </div>
    </div>
  </div>
</section>

<div class="tools-strip" role="img" aria-label="Row of salon tools: brushes, scissors, clippers and spray bottles"></div>
<div class="map" role="img" aria-label="Street map of the downtown district showing the salon location"></div>
<div class="map-marker"><span class="name">LUMORA</span><span class="sub">DOWNTOWN</span></div>
<svg class="map-pin" width="32" height="40" viewBox="0 0 32 40"><path d="M16 2a13 13 0 00-13 13c0 10 13 23 13 23s13-13 13-23A13 13 0 0016 2z" fill="#ffffff"/><circle cx="16" cy="15" r="5" fill="#3e392f"/></svg>

<section class="inquiry" role="group" aria-label="Quick inquiry form">
  <svg class="inquiry-icon" width="46" height="34" viewBox="0 0 46 34" fill="none" stroke="#fff" stroke-width="2.5"><rect x="2" y="2" width="42" height="30"/><path d="M2 2l21 17L44 2M2 32l15-15M44 32L29 17"/></svg>
  <div class="inquiry-title">QUICK<br>INQUIRY</div>
  <div class="field f-first">First Name*</div>
  <div class="field f-last">Last Name*</div>
  <div class="field f-phone">Your Phone*</div>
  <div class="field f-email">Your Email*</div>
  <div class="field f-msg">Message*</div>
  <div class="submit">SUBMIT NOW
    <svg width="48" height="44" viewBox="0 0 48 44" fill="none" stroke="#fff" stroke-width="1.6"><path d="M8 4l10 24M22 4L12 28"/><circle cx="10" cy="33" r="4"/><circle cx="20" cy="33" r="4"/><path d="M34 16l6 5-6 5z" fill="#fff"/></svg>
  </div>
</section>

<footer>
  <div class="copyright">Copyright © 2019 LUMORA DOWNTOWN. All Rights Reserved.</div>
  <div class="social" aria-label="Social links"><span></span><span></span><span></span><span></span><span></span></div>
</footer>

</body>
</html>
```